Website for Excavator and Earthworks Company

We require a modern, sleek and practical website for our newly created earthworks/excavator business in Perth, Western Australia called Gullwind Stonecut Earthworks.

The website should have a modern, cutting edge feel but only needs to be relatively simplistic in it's layout and eventual functionality.

Some pages it should have would be Home, About, Projects and Contact Us.

Number of Pages Required

1 page

```html
<!DOCTYPE html>
<html lang="en">
<head>
<meta charset="utf-8">
<title>Gullwind Stonecut Earthworks</title>
<link href="https://fonts.googleapis.com/css2?family=Archivo:wght@500;600;700;800&family=Work+Sans:wght@400;500;600&display=swap" rel="stylesheet">
<style>
:root{
  --accent:#cfe000;
  --ink:#141414;
  --black:#0b0b0b;
  --paper:#f4f4f2;
  --white:#ffffff;
  --muted:#6f6f6f;
  --line:#e2e2e2;
}
*{box-sizing:border-box;margin:0;padding:0}
html,body{width:1200px;height:3716px;overflow:hidden}
body{position:relative;background:var(--paper);font-family:"Work Sans",Arial,sans-serif;color:var(--ink)}
h1,h2,h3,.brand,.btn{font-family:"Archivo",Arial,sans-serif}

/* header */
.site-header{position:absolute;left:0;top:0;width:1200px;height:60px;background:var(--white);display:flex;align-items:center;padding:0 72px}
.brand{display:flex;align-items:center;gap:10px;font-weight:800;font-size:17px;color:var(--ink);letter-spacing:.5px;text-transform:uppercase}
.brand-square{width:22px;height:22px;background:var(--accent)}
.main-nav{position:absolute;left:370px;top:0;height:60px;display:flex;gap:34px;align-items:center;font-size:12px;text-transform:uppercase;color:#555}
.main-nav a{text-decoration:none;color:inherit;padding:6px 0}
.main-nav a.active{color:var(--ink);font-weight:600;border-bottom:2px solid var(--accent)}
.call-btn{position:absolute;right:72px;top:14px;width:120px;height:32px;background:var(--black);color:var(--white);font-size:12px;font-weight:700;display:flex;align-items:center;justify-content:center;letter-spacing:1px}

/* buttons */
.btn{display:inline-flex;align-items:center;justify-content:center;background:var(--accent);color:var(--ink);font-weight:700;font-size:12px;text-transform:uppercase;letter-spacing:.5px;clip-path:polygon(8% 0,100% 0,92% 100%,0 100%)}

/* hero */
.hero{position:absolute;left:0;top:60px;width:1200px;height:540px;background:linear-gradient(120deg,#33475f 0%,#5a7c9c 35%,#b7a56a 62%,#7a5a36 100%)}
.hero-shade{position:absolute;inset:0;background:linear-gradient(90deg,rgba(8,20,36,.8) 0%,rgba(8,20,36,.35) 45%,rgba(0,0,0,0) 70%)}
.hero h1{position:absolute;left:72px;top:175px;color:var(--white);font-size:48px;line-height:1.05;font-weight:800;text-transform:uppercase;width:600px}
.hero .tagline{position:absolute;left:72px;top:290px;color:var(--white);font-family:"Archivo",sans-serif;font-size:22px;font-weight:600;width:360px;line-height:1.3}
.hero .btn{position:absolute;left:72px;top:380px;width:150px;height:36px}

.values{position:absolute;left:72px;top:592px;width:1056px;height:48px;display:flex;gap:16px}
.value{flex:1;background:var(--white);display:flex;align-items:center;padding-left:24px;gap:12px;font-weight:600;font-size:17px}
.value i{display:block;width:6px;height:20px;background:var(--accent);transform:skewX(-20deg)}

/* about */
.about h2{position:absolute;left:72px;top:748px;font-size:34px;line-height:1.2;font-weight:600;text-transform:uppercase;letter-spacing:1px}
.about p{position:absolute;left:680px;top:750px;width:420px;font-size:13px;line-height:1.6;color:#555}
.photo{position:absolute}
.photo-city{left:72px;top:872px;width:788px;height:348px;background:linear-gradient(180deg,#7eb4e6 0%,#b9d6ef 50%,#8a9aa8 75%,#5d6a58 100%)}
.photo-mark{left:818px;top:1032px;width:304px;height:208px;background:linear-gradient(135deg,#7a7a7a,#3a3a3a)}
.accent-bar{position:absolute;left:72px;top:1220px;width:760px;height:8px;background:var(--accent)}
.accent-tab{position:absolute;left:860px;top:1000px;width:24px;height:32px;background:var(--accent)}

/* services */
.section-title{position:absolute;left:0;width:1200px;text-align:center;font-size:40px;font-weight:600;text-transform:uppercase;letter-spacing:1px}
.section-lead{position:absolute;left:300px;width:600px;text-align:center;font-size:13px;line-height:1.6;color:#777}
.service-grid{position:absolute;left:72px;top:1492px;width:1056px;display:grid;grid-template-columns:repeat(3,1fr);gap:20px 16px}
.service-card{background:var(--white);height:148px;padding:20px 16px;position:relative}
.service-icon{width:42px;height:34px;background:linear-gradient(135deg,#cfd3d8,#8d949b)}
.service-card h3{margin-top:22px;font-size:22px;font-weight:500;font-family:"Work Sans",sans-serif}
.read-more{margin-top:10px;font-size:12px;color:#444;display:flex;align-items:center;gap:8px}
.view-more{position:absolute;left:518px;width:164px;height:40px}

/* cta */
.photo-aerial{left:72px;top:2020px;width:1056px;height:360px;background:linear-gradient(160deg,#8b9a5a 0%,#a99068 40%,#6e7a44 70%,#4c5a2e 100%)}
.cta-box{position:absolute;left:72px;top:2360px;width:1056px;height:200px;background:var(--black);color:var(--white);padding:36px 48px}
.cta-box h2{font-size:34px;line-height:1.15;font-weight:700;text-transform:uppercase;width:720px}
.cta-box p{margin-top:16px;font-size:13px;line-height:1.6;color:#ccc;width:560px}
.cta-box .btn{position:absolute;right:48px;top:70px;width:180px;height:40px}

/* why */
.why-title{left:0;top:2640px}
.why-arrows{position:absolute;left:1048px;top:2650px;display:flex;gap:8px}
.why-arrows span{width:32px;height:32px;display:flex;align-items:center;justify-content:center}
.arrow-prev{background:var(--white)}
.arrow-next{background:var(--accent)}
.why-grid{position:absolute;left:72px;top:2732px;width:1056px;display:grid;grid-template-columns:repeat(3,1fr);gap:28px}
.why-card{height:312px;position:relative;color:var(--white)}
.why-card .label{position:absolute;left:18px;bottom:32px;font-size:22px;font-weight:500}
.why-card .more{position:absolute;left:18px;bottom:12px;font-size:12px;display:flex;gap:8px;align-items:center}
.why-1{background:linear-gradient(180deg,#6e8fb4,#2f4256)}
.why-2{background:linear-gradient(180deg,#e9ecef,#f3c21c 70%,#8a6f2a)}
.why-3{background:linear-gradient(180deg,#7f9dbf,#3d4a5a)}
.why-card .tint{position:absolute;inset:0;background:linear-gradient(180deg,rgba(0,0,0,0) 50%,rgba(0,0,0,.55))}

/* footer */
.site-footer{position:absolute;left:0;top:3248px;width:1200px;height:468px;background:var(--black);color:var(--white)}
.footer-brand{position:absolute;left:72px;top:60px;font-size:22px;color:var(--white)}
.footer-brand .brand-square{width:34px;height:34px}
.contact{position:absolute;left:72px;top:180px}
.contact h3{font-size:22px;font-weight:600;display:flex;gap:10px;align-items:center}
.contact h3 i{width:5px;height:18px;background:var(--accent);transform:skewX(-20deg)}
.contact ul{list-style:none;margin-top:28px;font-size:13px;color:#ddd;line-height:2}
.contact li{display:flex;align-items:center;gap:10px}
.footer-nav{position:absolute;left:72px;top:330px;font-size:13px;color:#ddd;display:flex;gap:12px}
.copyright{position:absolute;left:72px;top:420px;font-size:11px;color:#999}
.footer-rule{position:absolute;left:72px;top:380px;width:660px;height:1px;background:#333}

.contact-panel{position:absolute;left:760px;top:3220px;width:368px;height:496px;background:var(--white);padding:110px 36px 0}
.photo-hat{left:870px;top:3130px;width:150px;height:90px;background:linear-gradient(180deg,#f3c21c,#d89c0a)}
.contact-panel h2{text-align:center;font-size:28px;line-height:1.15;font-weight:700;text-transform:uppercase}
.field{margin-top:12px;border:1px solid #cfcfcf;height:34px;font-size:10px;color:#999;padding:10px}
.field:first-of-type{margin-top:24px}
.field.msg{height:64px}
.contact-panel .btn{position:absolute;right:36px;top:394px;width:140px;height:36px;background:var(--accent)}
.socials{position:absolute;right:36px;bottom:28px;display:flex;gap:10px}
.socials span{width:22px;height:22px;border-radius:50%;background:#1a1a1a}
</style>
</head>
<body>

<header class="site-header">
  <div class="brand"><span class="brand-square"></span>Gullwind Stonecut</div>
  <nav class="main-nav">
    <a class="active" href="#">Home</a>
    <a href="#">Our History</a>
    <a href="#">Our Services</a>
    <a href="#">Careers</a>
    <a href="#">Our Commitment</a>
  </nav>
  <div class="call-btn">CALL US</div>
</header>

<section class="hero">
  <div role="img" aria-label="Excavator bucket digging earth on a construction site under a blue sky" style="position:absolute;inset:0"></div>
  <div class="hero-shade"></div>
  <h1>Gullwind Stonecut Earthworks</h1>
  <p class="tagline">Modern Earthmoving For Perth's Growing Landscape</p>
  <span class="btn">Request a Quote</span>
</section>

<div class="values">
  <div class="value"><i></i>Integrity at our core</div>
  <div class="value"><i></i>Excellence in every project</div>
  <div class="value"><i></i>Trusted by clients for generations</div>
</div>

<section class="about">
  <h2>Built for precision.<br>Powered by experience.</h2>
  <p>Gullwind Stonecut Earthworks is a Perth-based excavation and earthworks company delivering reliable, high-quality site preparation for residential and commercial projects.</p>
  <div class="photo photo-city" role="img" aria-label="Perth city skyline with an arched footbridge over the river"></div>
  <div class="accent-tab"></div>
  <div class="photo photo-mark" role="img" aria-label="Monochrome site photo"></div>
  <div class="accent-bar"></div>
</section>

<section class="services">
  <h2 class="section-title" style="top:1360px">What we do</h2>
  <p class="section-lead" style="top:1414px">At Gullwind, we deliver top-tier infrastructure solutions with precision, efficiency, and innovation. Our services span multiple industries, ensuring reliability and excellence in every project.</p>
  <div class="service-grid">
    <div class="service-card"><div class="service-icon" role="img" aria-label="Excavation icon"></div><h3>Excavation</h3><div class="read-more">Read more <svg width="14" height="8" viewBox="0 0 14 8"><path d="M0 4h12M9 1l3 3-3 3" stroke="#222" fill="none"/></svg></div></div>
    <div class="service-card"><div class="service-icon" role="img" aria-label="Site preparation icon"></div><h3>Site Preparation</h3><div class="read-more">Read more <svg width="14" height="8" viewBox="0 0 14 8"><path d="M0 4h12M9 1l3 3-3 3" stroke="#222" fill="none"/></svg></div></div>
    <div class="service-card"><div class="service-icon" role="img" aria-label="Land clearing icon"></div><h3>Land Clearing</h3><div class="read-more">Read more <svg width="14" height="8" viewBox="0 0 14 8"><path d="M0 4h12M9 1l3 3-3 3" stroke="#222" fill="none"/></svg></div></div>
    <div class="service-card"><div class="service-icon" role="img" aria-label="Trenching icon"></div><h3>Trenching</h3><div class="read-more">Read more <svg width="14" height="8" viewBox="0 0 14 8"><path d="M0 4h12M9 1l3 3-3 3" stroke="#222" fill="none"/></svg></div></div>
    <div class="service-card"><div class="service-icon" role="img" aria-label="Grading and levelling icon"></div><h3>Grading &amp; Levelling</h3><div class="read-more">Read more <svg width="14" height="8" viewBox="0 0 14 8"><path d="M0 4h12M9 1l3 3-3 3" stroke="#222" fill="none"/></svg></div></div>
    <div class="service-card"><div class="service-icon" role="img" aria-label="Driveways and pads icon"></div><h3>Driveways &amp; Pads</h3><div class="read-more">Read more <svg width="14" height="8" viewBox="0 0 14 8"><path d="M0 4h12M9 1l3 3-3 3" stroke="#222" fill="none"/></svg></div></div>
  </div>
  <span class="btn view-more" style="top:1864px">View More</span>
</section>

<section class="cta">
  <div class="photo photo-aerial" role="img" aria-label="Aerial view of a cleared earthworks site beside a road"></div>
  <div class="cta-box">
    <h2>Have a site that needs clearing, excavation, or preparation?</h2>
    <p>Tell us what you're building and we'll take care of the ground beneath it. Whether it's residential or commercial, small or large – we're ready.</p>
    <span class="btn">Get a Free Quote</span>
  </div>
</section>

<section class="why">
  <h2 class="section-title why-title">Why Gullwind Stonecut</h2>
  <div class="why-arrows">
    <span class="arrow-prev"><svg width="10" height="12" viewBox="0 0 10 12"><path d="M8 1L2 6l6 5" stroke="#111" stroke-width="2" fill="none"/></svg></span>
    <span class="arrow-next"><svg width="10" height="12" viewBox="0 0 10 12"><path d="M2 1l6 5-6 5" stroke="#111" stroke-width="2" fill="none"/></svg></span>
  </div>
  <div class="why-grid">
    <div class="why-card why-1" role="img" aria-label="Perth city skyline at dusk"><div class="tint"></div><span class="label">Locally based in Perth</span><span class="more">Read more →</span></div>
    <div class="why-card why-2" role="img" aria-label="Yellow hard hat and ear protection on a table"><div class="tint"></div><span class="label">Safety-first job sites</span><span class="more">Read more →</span></div>
    <div class="why-card why-3" role="img" aria-label="Electrical transmission towers against the sky"><div class="tint"></div><span class="label">Reliable scheduling</span><span class="more">Read more →</span></div>
  </div>
  <span class="btn view-more" style="top:3100px">View More</span>
</section>

<footer class="site-footer">
  <div class="brand footer-brand"><span class="brand-square"></span>Gullwind Stonecut</div>
  <div class="contact">
    <h3><i></i>Contact Details</h3>
    <ul>
      <li><svg width="12" height="14" viewBox="0 0 12 14"><path d="M6 13S1 8 1 5a5 5 0 0110 0c0 3-5 8-5 8z" fill="#cfe000"/><circle cx="6" cy="5" r="1.8" fill="#0b0b0b"/></svg>PO Box 4821 Perth, Australia</li>
      <li><svg width="14" height="10" viewBox="0 0 14 10"><rect x=".5" y=".5" width="13" height="9" fill="none" stroke="#cfe000"/><path d="M.5 .5L7 6l6.5-5.5" fill="none" stroke="#cfe000"/></svg>info@gullwindstonecut.au &nbsp;&nbsp;
        <svg width="12" height="12" viewBox="0 0 12 12"><path d="M2 1l2 0 1 3-1.5 1a7 7 0 003.5 3.5L8 7l3 1v2c0 1-1 1-1 1A9 9 0 011 2s0-1 1-1z" fill="#cfe000"/></svg>08 5550 1234</li>
    </ul>
  </div>
  <nav class="footer-nav"><span>Home</span>|<span>About</span>|<span>Services</span>|<span>Careers</span>|<span>Projects</span>|<span>Contact</span></nav>
  <div class="footer-rule"></div>
  <p class="copyright">Copyright © Gullwind Stonecut. All rights reserved.</p>
</footer>

<div class="photo photo-hat" role="img" aria-label="Yellow safety hard hat"></div>
<aside class="contact-panel">
  <h2>Ready to start<br>your project?</h2>
  <div class="field">First Name</div>
  <div class="field">Email Address</div>
  <div class="field msg">Enter Your Message</div>
  <span class="btn">Send Message</span>
  <div class="socials"><span></span><span></span><span></span></div>
</aside>

</body>
</html>
```